Business Cards for Internet Security Company

Awesome designers! This is the opportunity to help design cards for a forward thinking network security company. They use threat information gathered from peer groups to make intelligent decisions on what threats are relevant and which arent. ( not that you need this to do designs, but just so you know where they are coming from. ) :-)

We'd like to see a two side design and the deliverables will be in illustrator 4. The logo is attached and the logo colors are attached in the JPG and I've attached a an eps of the logo and icon

```html
<!DOCTYPE html>
<html lang="en">
<head>
<meta charset="utf-8">
<title>Corvane Business Cards</title>
<link rel="stylesheet" href="https://fonts.googleapis.com/css2?family=Questrial&display=swap">
<style>
  :root {
    --backdrop: #2b2b2d;
    --card: #2a2829;
    --card-edge: #353334;
    --brand-blue: #3a7fb0;
    --brand-blue-deep: #2f6f98;
    --text-muted: #8a8a8e;
    --rule: #3d5a70;
  }
  * { margin: 0; padding: 0; box-sizing: border-box; }
  html, body {
    width: 1200px;
    height: 900px;
    overflow: hidden;
    background: var(--backdrop);
    font-family: "Questrial", Arial, sans-serif;
  }
  .stage {
    position: relative;
    width: 1200px;
    height: 900px;
  }
  .card {
    position: absolute;
    top: 301px;
    width: 520px;
    height: 298px;
    background: var(--card);
    border: 1px solid var(--card-edge);
    box-shadow: 0 18px 40px rgba(0,0,0,0.45);
  }
  .card--back { left: 60px; }
  .card--front { left: 620px; }

  .wordmark {
    display: flex;
    align-items: center;
    color: var(--brand-blue);
    letter-spacing: 0.5px;
  }
  .wordmark__dot {
    border-radius: 50%;
    background: var(--brand-blue);
    flex: none;
  }

  /* back: contact side */
  .card--back .wordmark {
    position: absolute;
    left: 44px;
    top: 30px;
    font-size: 40px;
  }
  .card--back .wordmark__dot { width: 30px; height: 30px; margin-right: 10px; }
  .contact-name {
    position: absolute;
    left: 46px;
    top: 104px;
    color: var(--brand-blue);
    font-size: 20px;
  }
  .contact-role {
    position: absolute;
    left: 46px;
    top: 132px;
    color: var(--brand-blue);
    font-size: 13px;
  }
  .contact-address {
    position: absolute;
    left: 46px;
    top: 176px;
    color: var(--text-muted);
    font-size: 11.5px;
    line-height: 16px;
  }
  .contact-line {
    display: flex;
    align-items: center;
    gap: 6px;
  }
  .contact-line svg { width: 11px; height: 11px; fill: var(--text-muted); }
  .contact-rule {
    position: absolute;
    left: 40px;
    right: 40px;
    top: 236px;
    height: 1px;
    background: var(--rule);
  }
  .contact-extra {
    position: absolute;
    right: 46px;
    top: 196px;
    color: var(--text-muted);
    font-size: 11.5px;
    line-height: 18px;
  }
  .contact-extra--mail { top: 246px; }

  /* front: brand side */
  .card--front .wordmark {
    position: absolute;
    left: 0;
    right: 0;
    top: 0;
    bottom: 0;
    justify-content: center;
    font-size: 84px;
    color: var(--brand-blue-deep);
  }
  .card--front .wordmark__dot { width: 58px; height: 58px; margin-right: 18px; background: var(--brand-blue); }
</style>
</head>
<body>
<main class="stage">
  <section class="card card--back" aria-label="Card back, contact details">
    <div class="wordmark"><span class="wordmark__dot"></span>Corvane</div>
    <p class="contact-name">Dario Menzel</p>
    <p class="contact-role">Managing Director</p>
    <div class="contact-address">
      <p>210 Harbor Point Dr</p>
      <p>Easton, OH 44021</p>
      <p class="contact-line">
        <svg viewBox="0 0 12 12" aria-hidden="true"><rect x="3" y="0" width="6" height="12" rx="1.2"/></svg>
        555-201-4830
      </p>
    </div>
    <div class="contact-rule"></div>
    <p class="contact-extra contact-line">
      <svg viewBox="0 0 12 12" aria-hidden="true"><rect x="3" y="0" width="6" height="4"/><rect x="0" y="4" width="12" height="5" rx="1"/><rect x="3" y="8" width="6" height="4"/></svg>
      555-201-4831
    </p>
    <p class="contact-extra contact-extra--mail contact-line">
      <svg viewBox="0 0 12 12" aria-hidden="true"><path d="M0 2h12v8H0z M1 3l5 4 5-4" fill="none" stroke="#8a8a8e" stroke-width="1.2"/></svg>
      dario@corvane.com
    </p>
  </section>

  <section class="card card--front" aria-label="Card front, brand">
    <div class="wordmark"><span class="wordmark__dot"></span>Corvane</div>
  </section>
</main>
</body>
</html>
```